TRV Electrical – Fridge Magnet & Letterbox Leaflet

Overview
We are a local electrical contractor based in Gooseberry Hill in the Perth Hills (Western Australia).
We are looking for a designer to create:
1️⃣ A fridge magnet design
2️⃣ A matching letterbox leaflet (A6 or DL)
The goal is to create clean, professional marketing that feels local and trustworthy, not flashy advertising.
The designs must feel like a high-quality local trades business, appealing to homeowners in suburbs such as:
Kalamunda
Gooseberry Hill
Lesmurdie
Walliston
Pickering Brook
Design Style
The design should feel:
✔ Local
✔ Authentic
✔ Professional
✔ Trustworthy
✔ Clean and simple
NOT:
✖ Cheap advertising
✖ Overly flashy
✖ Busy or cluttered
Think premium local tradesman, not mass marketing.
Branding
Use our brand colours inspired by our van:
Primary colours
Navy Blue
White
Accent colour
Yellow / gold highlight
Design should match the look of our work van branding.
Images Provided
We will provide:
✔ Company logo
✔ Photo of our branded van in the Perth Hills
The van photo should be used in the leaflet design to reinforce our local presence.
Fridge Magnet Design
Size suggestion:
90mm x 55mm
Purpose:
Homeowners keep this magnet so they can easily call a trusted electrician.
Must include:
TRV Electrical Contracting
Local Perth Hills Electrician
Based in Gooseberry Hill
Phone number (large and clear)
📞 0472 615 904
Services:
• Fault finding
• Switchboard upgrades
• Lighting & power
• Ceiling fans
• Smoke alarm compliance
Also include:
⭐ 110+ Rovlix Reviews
Website:
www.trvelectrical-example.com.au
Design should be very simple and easy to read from across a kitchen.
Leaflet Design
Size options:
A6 or DL
Purpose:
Letterbox drop marketing in Perth Hills suburbs.
Front Side
Headline:
WE'RE WORKING IN YOUR AREA
Subtext:
Local electrician based in Gooseberry Hill
Include:
✔ Photo of our van
✔ TRV logo
✔ Key services
Services:
• Fault finding
• Switchboard upgrades
• Lighting & power
• Ceiling fans
• Smoke alarm compliance
Call to action:
📞 Call Dorian – 0472 615 904
⭐ 110+ Five-Star Rovlix Reviews
Back Side
Headline:
Your Local Perth Hills Electrician
Servicing:
Kalamunda
Gooseberry Hill
Lesmurdie
Walliston
Pickering Brook
Short message:
Reliable electrical work across the Perth Hills.
Call Dorian
📞 0472 615 904
Website:
www.trvelectrical-example.com.au
EC47286
Target Audience
Homeowners in the Perth Hills aged 35–70.
Many homes are older properties and often need electrical upgrades, repairs and safety work.
Design should appeal to homeowners who value reliability and local service.
Deliverables
Designers must provide:
✔ Print-ready files
✔ Editable source files
✔ High resolution files
For:
Fridge magnet
Leaflet front and back
Final Notes
This design should communicate:
✔ Trusted local electrician
✔ Established business
✔ Professional service
✔ Easy to contact
The goal is to create marketing people will keep, not throw away.

```html
<!DOCTYPE html>
<html lang="en">
<head>
<meta charset="utf-8">
<title>TRV Electrical – Leaflet &amp; Magnet</title>
<link rel="stylesheet" href="https://fonts.googleapis.com/css2?family=Poppins:ital,wght@0,400;0,500;0,600;0,700;0,800;1,600&display=swap">
<style>
:root{
  --navy:#1f2a5c;
  --navy-deep:#18214d;
  --gold:#d9a92c;
  --gold-light:#f0c44a;
  --white:#ffffff;
  --board:#6b6b6b;
  --grey-bar:#ececec;
  --ink:#2b2b2b;
  --map:#d9d9d9;
}
*{margin:0;padding:0;box-sizing:border-box}
html,body{width:1200px;height:644px;overflow:hidden}
body{background:var(--board);font-family:"Poppins",sans-serif;position:relative}
.board-label{position:absolute;top:20px;color:var(--white);font-weight:600;font-size:19px;letter-spacing:.5px;text-align:center}
.piece{position:absolute;background:var(--white);overflow:hidden}
.flyer{top:49px;width:396px;height:558px}
.flyer--front{left:47px}
.flyer--back{left:473px}
.magnet{left:904px;top:48px;width:254px;height:414px}

/* brand lockup */
.brand{position:absolute;display:flex;align-items:center}
.brand-square{background:var(--navy);border-radius:4px}
.brand-name{color:var(--navy);font-weight:500;line-height:1.15}
.flyer .brand{left:115px;top:11px;gap:12px}
.flyer .brand-square{width:45px;height:64px}
.flyer .brand-name{font-size:17px}
.magnet .brand{left:66px;top:9px;gap:9px}
.magnet .brand-square{width:21px;height:48px}
.magnet .brand-name{font-size:12px}

/* headline band */
.band{position:absolute;left:0;right:0;background:var(--navy);color:var(--white);font-weight:800;display:flex;align-items:center;justify-content:center;text-transform:uppercase;white-space:nowrap}
.flyer .band{top:89px;height:36px;font-size:21px}
.flyer--back .band{font-size:17.5px}
.magnet .band{top:65px;height:24px;font-size:12.5px;font-weight:700}

/* photo area */
.photo{position:absolute;left:0;right:0;background:linear-gradient(180deg,#b9cde0 0%,#8fa3a0 35%,#2a3466 55%,#2a3466 75%,#a5825a 100%)}
.flyer .photo{top:125px;height:212px}
.magnet .photo{top:89px;height:151px}
.ribbon{position:absolute;background:linear-gradient(90deg,var(--gold),var(--gold-light),var(--gold));color:var(--navy);font-weight:700;display:flex;align-items:center;justify-content:center;white-space:nowrap;clip-path:polygon(3% 0,100% 0,97% 100%,0 100%)}
.flyer .ribbon{left:35px;top:125px;width:326px;height:22px;font-size:13.5px}
.magnet .ribbon{left:44px;top:89px;width:170px;height:19px;font-size:10.5px;color:var(--white)}
.gold-rule{position:absolute;left:0;right:0;height:3px;background:var(--gold)}
.flyer .gold-rule{top:336px}
.magnet .gold-rule{top:239px}

/* section tab */
.tab{position:absolute;background:var(--navy);color:var(--white);font-weight:600;display:flex;align-items:center;justify-content:center;text-transform:uppercase}
.flyer .tab{left:136px;top:321px;width:132px;height:29px;font-size:21px}
.magnet .tab{left:85px;top:230px;width:86px;height:19px;font-size:13.5px}

/* services */
.service{position:absolute;display:flex;flex-direction:column;align-items:center;text-align:center;color:var(--ink);transform:translateX(-50%);white-space:nowrap}
.flyer .service{top:366px;font-size:11px;line-height:1.2}
.flyer .service svg{width:49px;height:43px;margin-bottom:10px}
.magnet .service{top:261px;font-size:6.6px;line-height:1.25}
.magnet .service svg{width:31px;height:28px;margin-bottom:6px}
.hex{fill:var(--navy)}
.hex-glyph{fill:none;stroke:var(--white);stroke-width:2.2}
.divider{position:absolute;top:366px;height:44px;border-left:1.5px dotted var(--gold)}

/* reviews */
.reviews{position:absolute;background:var(--grey-bar);color:var(--ink);font-weight:600;display:flex;align-items:center;justify-content:center;gap:6px;text-transform:uppercase;white-space:nowrap}
.reviews .stars{color:var(--gold);letter-spacing:1px}
.flyer .reviews{left:25px;top:453px;width:352px;height:26px;font-size:14.5px}
.magnet .reviews{left:15px;top:326px;width:228px;height:15px;font-size:9.5px;gap:4px;z-index:2}

/* flyer footer */
.footer{position:absolute;left:0;right:0;top:499px;height:39px;background:var(--navy)}
.footer-gold{position:absolute;left:0;top:0;width:70px;height:39px;background:linear-gradient(90deg,var(--gold),var(--gold-light))}
.footer-call{position:absolute;left:28px;top:0;width:190px;height:39px;background:var(--white);clip-path:polygon(0 0,93% 0,100% 100%,0 100%);border-top:1px solid var(--gold)}
.footer-slant{position:absolute;left:197px;top:0;width:24px;height:39px;background:var(--gold);clip-path:polygon(0 0,30% 0,100% 100%,70% 100%)}
.phone-disc{position:absolute;left:16px;top:2px;width:35px;height:35px;border-radius:50%;background:var(--navy);border:2px solid var(--gold);display:flex;align-items:center;justify-content:center}
.phone-disc svg{width:16px;height:16px}
.call-label{position:absolute;left:58px;top:2px;font-size:12px;font-weight:700;color:var(--navy);line-height:1}
.call-number{position:absolute;left:57px;top:14px;font-size:20px;font-weight:800;color:var(--navy);line-height:1;white-space:nowrap}
.licence{position:absolute;left:224px;top:6px;color:var(--white);font-size:11.5px;font-weight:600;line-height:1}
.site{position:absolute;left:224px;top:22px;color:var(--white);font-size:8px;font-weight:500;line-height:1;display:flex;align-items:center;gap:3px;white-space:nowrap}
.site svg{width:8px;height:8px}

/* back side */
.map{position:absolute;left:95px;top:135px;width:282px;height:277px;background:radial-gradient(ellipse at 55% 45%,#e4e4e4 0%,var(--map) 60%,#ffffff 100%)}
.flyer--back .tab{left:34px;top:344px;width:146px;height:28px;font-size:21px}
.suburbs{position:absolute;left:36px;top:381px;display:grid;grid-template-columns:109px 109px;row-gap:3px;color:var(--navy);font-size:10.5px;font-weight:600;list-style:none}
.suburb{display:flex;align-items:center;gap:5px;height:13px;white-space:nowrap}
.suburb svg{width:11px;height:11px}
.tagline{position:absolute;left:0;right:0;top:457px;text-align:center;font-style:italic;font-weight:600;font-size:15.5px;color:var(--navy);white-space:nowrap}
.tagline em{color:var(--gold)}

/* magnet contact */
.magnet-call{position:absolute;left:0;right:0;top:334px;height:52px;background:var(--navy);display:flex;align-items:center;justify-content:center;gap:6px;padding-top:6px}
.magnet-call .phone-tile{width:21px;height:23px;background:var(--gold);border-radius:4px;display:flex;align-items:center;justify-content:center}
.magnet-call .phone-tile svg{width:14px;height:14px}
.magnet-number{color:var(--white);font-size:29px;font-weight:700;letter-spacing:.3px;line-height:1;white-space:nowrap}
.magnet-web{position:absolute;left:0;right:0;top:386px;height:28px;background:var(--gold);color:var(--white);font-weight:600;font-size:12px;display:flex;align-items:center;justify-content:center;gap:4px;white-space:nowrap}
.magnet-web svg{width:12px;height:12px}
</style>
</head>
<body>

<div class="board-label" style="left:47px;width:396px">FLYER FRONT</div>
<div class="board-label" style="left:473px;width:396px">FLYER BACK</div>
<div class="board-label" style="left:904px;width:254px">MAGNET</div>

<!-- Leaflet front -->
<section class="piece flyer flyer--front">
  <div class="brand"><span class="brand-square"></span><span class="brand-name">TRV Electrical<br>Contracting</span></div>
  <h1 class="band">We're working in your area</h1>
  <div class="photo" role="img" aria-label="Photo of the branded navy and white TRV work van parked among gum trees in the Perth Hills"></div>
  <div class="ribbon">Local electrician based in Gooseberry Hill</div>
  <div class="gold-rule"></div>
  <h2 class="tab">Services</h2>

  <div class="service" style="left:53px"><svg viewBox="0 0 49 43"><polygon class="hex" points="12,0 37,0 49,21.5 37,43 12,43 0,21.5"/><circle class="hex-glyph" cx="23" cy="20" r="8"/><line class="hex-glyph" x1="29" y1="26" x2="34" y2="31"/></svg>Fault finding</div>
  <div class="divider" style="left:93px"></div>
  <div class="service" style="left:132px"><svg viewBox="0 0 49 43"><polygon class="hex" points="12,0 37,0 49,21.5 37,43 12,43 0,21.5"/><rect class="hex-glyph" x="15" y="11" width="19" height="21"/><line class="hex-glyph" x1="15" y1="21.5" x2="34" y2="21.5"/></svg>Switchboard<br>upgrades</div>
  <div class="divider" style="left:170px"></div>
  <div class="service" style="left:207px"><svg viewBox="0 0 49 43"><polygon class="hex" points="12,0 37,0 49,21.5 37,43 12,43 0,21.5"/><circle class="hex-glyph" cx="24.5" cy="18" r="7"/><line class="hex-glyph" x1="21" y1="29" x2="28" y2="29"/></svg>Lighting<br>&amp; power</div>
  <div class="divider" style="left:242px"></div>
  <div class="service" style="left:278px"><svg viewBox="0 0 49 43"><polygon class="hex" points="12,0 37,0 49,21.5 37,43 12,43 0,21.5"/><line class="hex-glyph" x1="24.5" y1="9" x2="24.5" y2="22"/><line class="hex-glyph" x1="12" y1="24" x2="37" y2="20"/></svg>Ceiling<br>fans</div>
  <div class="divider" style="left:313px"></div>
  <div class="service" style="left:347px"><svg viewBox="0 0 49 43"><polygon class="hex" points="12,0 37,0 49,21.5 37,43 12,43 0,21.5"/><ellipse class="hex-glyph" cx="24.5" cy="18" rx="10" ry="5"/><line class="hex-glyph" x1="17" y1="27" x2="32" y2="27"/></svg>Smoke alarm<br>compliance</div>

  <div class="reviews"><span class="stars">★★★★★</span>110+ Five-Star Rovlix Reviews</div>

  <footer class="footer">
    <div class="footer-gold"></div>
    <div class="footer-call"></div>
    <div class="footer-slant"></div>
    <div class="phone-disc"><svg viewBox="0 0 24 24"><path fill="#fff" d="M6.6 10.8a15 15 0 0 0 6.6 6.6l2.2-2.2a1 1 0 0 1 1-.25 11.4 11.4 0 0 0 3.6.57 1 1 0 0 1 1 1V20a1 1 0 0 1-1 1A17 17 0 0 1 3 4a1 1 0 0 1 1-1h3.5a1 1 0 0 1 1 1c0 1.25.2 2.45.57 3.57a1 1 0 0 1-.25 1z"/></svg></div>
    <span class="call-label">Call Dorian</span>
    <span class="call-number">0472 615 904</span>
    <span class="licence">EC47286</span>
    <span class="site"><svg viewBox="0 0 24 24"><circle cx="12" cy="12" r="10" fill="none" stroke="#fff" stroke-width="2"/><path d="M2 12h20M12 2c3 3 3 17 0 20M12 2c-3 3-3 17 0 20" fill="none" stroke="#fff" stroke-width="1.5"/></svg>www.trvelectrical-example.com.au</span>
  </footer>
</section>

<!-- Leaflet back -->
<section class="piece flyer flyer--back">
  <div class="brand"><span class="brand-square"></span><span class="brand-name">TRV Electrical<br>Contracting</span></div>
  <h1 class="band">Your local Perth Hills electrician</h1>
  <div class="map" role="img" aria-label="Dotted map of Australia with gold markers on the Perth Hills suburbs served"></div>
  <h2 class="tab">Servicing</h2>
  <ul class="suburbs">
    <li class="suburb"><svg viewBox="0 0 12 12"><circle cx="6" cy="6" r="5" fill="none" stroke="#d9a92c" stroke-width="1.2"/><path d="M3.5 6.2l1.8 1.8 3.2-3.5" fill="none" stroke="#d9a92c" stroke-width="1.2"/></svg>Kalamunda</li>
    <li class="suburb"><svg viewBox="0 0 12 12"><circle cx="6" cy="6" r="5" fill="none" stroke="#d9a92c" stroke-width="1.2"/><path d="M3.5 6.2l1.8 1.8 3.2-3.5" fill="none" stroke="#d9a92c" stroke-width="1.2"/></svg>Walliston</li>
    <li class="suburb"><svg viewBox="0 0 12 12"><circle cx="6" cy="6" r="5" fill="none" stroke="#d9a92c" stroke-width="1.2"/><path d="M3.5 6.2l1.8 1.8 3.2-3.5" fill="none" stroke="#d9a92c" stroke-width="1.2"/></svg>Gooseberry Hill</li>
    <li class="suburb"><svg viewBox="0 0 12 12"><circle cx="6" cy="6" r="5" fill="none" stroke="#d9a92c" stroke-width="1.2"/><path d="M3.5 6.2l1.8 1.8 3.2-3.5" fill="none" stroke="#d9a92c" stroke-width="1.2"/></svg>Pickering Brook</li>
    <li class="suburb"><svg viewBox="0 0 12 12"><circle cx="6" cy="6" r="5" fill="none" stroke="#d9a92c" stroke-width="1.2"/><path d="M3.5 6.2l1.8 1.8 3.2-3.5" fill="none" stroke="#d9a92c" stroke-width="1.2"/></svg>Lesmurdie</li>
  </ul>
  <p class="tagline">Reliable electrical work across the <em>Perth Hills.</em></p>

  <footer class="footer">
    <div class="footer-gold"></div>
    <div class="footer-call"></div>
    <div class="footer-slant"></div>
    <div class="phone-disc"><svg viewBox="0 0 24 24"><path fill="#fff" d="M6.6 10.8a15 15 0 0 0 6.6 6.6l2.2-2.2a1 1 0 0 1 1-.25 11.4 11.4 0 0 0 3.6.57 1 1 0 0 1 1 1V20a1 1 0 0 1-1 1A17 17 0 0 1 3 4a1 1 0 0 1 1-1h3.5a1 1 0 0 1 1 1c0 1.25.2 2.45.57 3.57a1 1 0 0 1-.25 1z"/></svg></div>
    <span class="call-label">Call Dorian</span>
    <span class="call-number">0472 615 904</span>
    <span class="licence">EC47286</span>
    <span class="site"><svg viewBox="0 0 24 24"><circle cx="12" cy="12" r="10" fill="none" stroke="#fff" stroke-width="2"/><path d="M2 12h20M12 2c3 3 3 17 0 20M12 2c-3 3-3 17 0 20" fill="none" stroke="#fff" stroke-width="1.5"/></svg>www.trvelectrical-example.com.au</span>
  </footer>
</section>

<!-- Fridge magnet -->
<section class="piece magnet">
  <div class="brand"><span class="brand-square"></span><span class="brand-name">TRV Electrical<br>Contracting</span></div>
  <h1 class="band">Local Perth Hills electrician</h1>
  <div class="photo" role="img" aria-label="Photo of the branded TRV work van in the Perth Hills"></div>
  <div class="ribbon">Based in Gooseberry Hill</div>
  <div class="gold-rule"></div>
  <h2 class="tab">Services</h2>

  <div class="service" style="left:32px"><svg viewBox="0 0 49 43"><polygon class="hex" points="12,0 37,0 49,21.5 37,43 12,43 0,21.5"/><circle class="hex-glyph" cx="23" cy="20" r="8"/><line class="hex-glyph" x1="29" y1="26" x2="34" y2="31"/></svg>Fault finding</div>
  <div class="service" style="left:84px"><svg viewBox="0 0 49 43"><polygon class="hex" points="12,0 37,0 49,21.5 37,43 12,43 0,21.5"/><rect class="hex-glyph" x="15" y="11" width="19" height="21"/><line class="hex-glyph" x1="15" y1="21.5" x2="34" y2="21.5"/></svg>Switchboard<br>upgrades</div>
  <div class="service" style="left:131px"><svg viewBox="0 0 49 43"><polygon class="hex" points="12,0 37,0 49,21.5 37,43 12,43 0,21.5"/><circle class="hex-glyph" cx="24.5" cy="18" r="7"/><line class="hex-glyph" x1="21" y1="29" x2="28" y2="29"/></svg>Lighting<br>&amp; power</div>
  <div class="service" style="left:176px"><svg viewBox="0 0 49 43"><polygon class="hex" points="12,0 37,0 49,21.5 37,43 12,43 0,21.5"/><line class="hex-glyph" x1="24.5" y1="9" x2="24.5" y2="22"/><line class="hex-glyph" x1="12" y1="24" x2="37" y2="20"/></svg>Ceiling<br>fans</div>
  <div class="service" style="left:224px"><svg viewBox="0 0 49 43"><polygon class="hex" points="12,0 37,0 49,21.5 37,43 12,43 0,21.5"/><ellipse class="hex-glyph" cx="24.5" cy="18" rx="10" ry="5"/><line class="hex-glyph" x1="17" y1="27" x2="32" y2="27"/></svg>Smoke alarm<br>compliance</div>

  <div class="reviews"><span class="stars">★★★★★</span>110+ Five-Star Rovlix Reviews</div>
  <div class="magnet-call">
    <span class="phone-tile"><svg viewBox="0 0 24 24"><path fill="#1f2a5c" d="M6.6 10.8a15 15 0 0 0 6.6 6.6l2.2-2.2a1 1 0 0 1 1-.25 11.4 11.4 0 0 0 3.6.57 1 1 0 0 1 1 1V20a1 1 0 0 1-1 1A17 17 0 0 1 3 4a1 1 0 0 1 1-1h3.5a1 1 0 0 1 1 1c0 1.25.2 2.45.57 3.57a1 1 0 0 1-.25 1z"/></svg></span>
    <span class="magnet-number">0472 615 904</span>
  </div>
  <div class="magnet-web"><svg viewBox="0 0 24 24"><circle cx="12" cy="12" r="10" fill="none" stroke="#fff" stroke-width="2"/><path d="M2 12h20M12 2c3 3 3 17 0 20M12 2c-3 3-3 17 0 20" fill="none" stroke="#fff" stroke-width="1.5"/></svg>www.trvelectrical-example.com.au</div>
</section>

</body>
</html>
```